Business card for a new cabinet shop company named Torvane Cabinets for high end cabinets

Design a business card, thinking dark rich green with colours to speak of high end luxury ie; cream, gold, black possibly

Miles Harwick
Director Craftsman
Email: info@torvanecabinets.com.au
Instagram : @torvane.cabinets

```html
<!DOCTYPE html>
<html lang="en">
<head>
<meta charset="utf-8">
<title>Torvane Cabinets — Business Card</title>
<link href="https://fonts.googleapis.com/css2?family=Montserrat:wght@400;500;700&display=swap" rel="stylesheet">
<style>
  :root {
    --stage: #161616;
    --card-green: #1f3d3b;
    --gold: #c9a862;
    --cream-white: #ffffff;
    --card-w: 690px;
    --card-h: 394px;
    --radius: 24px;
  }
  * { box-sizing: border-box; margin: 0; padding: 0; }
  html, body {
    width: 1200px;
    height: 1059px;
    overflow: hidden;
    background: var(--stage);
    font-family: "Montserrat", sans-serif;
  }
  .card {
    position: absolute;
    left: 255px;
    width: var(--card-w);
    height: var(--card-h);
    background: var(--card-green);
    border-radius: var(--radius);
    overflow: hidden;
  }
  .card--front { top: 99px; }
  .card--back { top: 553px; }

  .wordmark {
    position: absolute;
    color: var(--gold);
    font-weight: 400;
    line-height: 1;
  }
  .wordmark__name { display: block; letter-spacing: 0.5px; }
  .wordmark__sub { display: block; text-transform: uppercase; }

  .card--front .wordmark {
    right: 42px;
    top: 52px;
    text-align: right;
  }
  .card--front .wordmark__name { font-size: 50px; }
  .card--front .wordmark__sub { font-size: 22px; letter-spacing: 10px; margin-top: 12px; margin-right: -10px; }

  .card--back .wordmark {
    left: 0;
    right: 0;
    top: 128px;
    text-align: center;
  }
  .card--back .wordmark__name { font-size: 72px; }
  .card--back .wordmark__sub { font-size: 32px; letter-spacing: 14px; margin-top: 16px; margin-right: -14px; }

  .person {
    position: absolute;
    left: 52px;
    top: 204px;
  }
  .person__name {
    color: var(--gold);
    font-weight: 700;
    font-size: 30px;
    line-height: 1.1;
  }
  .person__role {
    color: var(--cream-white);
    font-weight: 400;
    font-size: 18px;
    margin-top: 8px;
    margin-left: 2px;
  }
  .divider {
    position: absolute;
    left: 53px;
    width: 593px;
    top: 286px;
    height: 1.5px;
    background: var(--cream-white);
  }
  .contact-email {
    position: absolute;
    left: 53px;
    top: 310px;
    display: flex;
    align-items: center;
    gap: 8px;
    color: var(--cream-white);
    font-size: 18px;
  }
  .contact-email svg { width: 18px; height: 13px; }

  .footer-band {
    position: absolute;
    left: 0;
    top: 0;
    width: var(--card-w);
    height: var(--card-h);
  }
  .social {
    position: absolute;
    left: 460px;
    top: 364px;
    display: flex;
    align-items: center;
    gap: 9px;
    color: var(--card-green);
    font-size: 17px;
    font-weight: 500;
  }
  .social__dot {
    width: 14px;
    height: 14px;
    border: 2px solid var(--card-green);
    border-radius: 50%;
  }
</style>
</head>
<body>

  <section class="card card--front" aria-label="Business card front">
    <svg class="footer-band" viewBox="0 0 690 394" aria-hidden="true">
      <path fill="var(--gold)" d="M0 394 L0 379 Q200 382 385 378 Q405 376 420 367 L434 359 Q440 356 452 356 L690 356 L690 394 Z"/>
      <path fill="var(--cream-white)" d="M0 363 L420 363 Q410 371 395 375 Q300 379 0 378 Z"/>
    </svg>

    <div class="wordmark">
      <span class="wordmark__name">Torvane</span>
      <span class="wordmark__sub">Cabinets</span>
    </div>

    <div class="person">
      <h1 class="person__name">Miles Harwick</h1>
      <p class="person__role">Director Craftsman</p>
    </div>

    <div class="divider"></div>

    <p class="contact-email">
      <svg viewBox="0 0 18 13" aria-hidden="true">
        <rect width="18" height="13" fill="var(--gold)"/>
        <path d="M1 1.5 L9 7.5 L17 1.5" fill="none" stroke="var(--card-green)" stroke-width="1.8"/>
      </svg>
      info@torvanecabinets.com.au
    </p>

    <p class="social">
      <span class="social__dot" aria-hidden="true"></span>
      @torvane.cabinets
    </p>
  </section>

  <section class="card card--back" aria-label="Business card back">
    <div class="wordmark">
      <span class="wordmark__name">Torvane</span>
      <span class="wordmark__sub">Cabinets</span>
    </div>
  </section>

</body>
</html>
```